Business Card Design Project

Looking for a simple and stylish business card. We are an Advertising Company. The card Must feature the company logo (attached) and also this info.
p: 0461528390
e: sales@jh-promo.com.au
w: www.jh-promo.com.au
We Advertise mainly using TV screens featured in restaurants and cafe. See website for more about the business.
Not really looking for a plain background, but at the same time do not want to much happening in the Background. I am not really to fussy though with the design or the colour scheme, and I am leaving the creativity part up to you creative designers.
Business

```html
<!DOCTYPE html>
<html lang="en">
<head>
<meta charset="utf-8">
<title>JH Promo Business Card</title>
<link href="https://fonts.googleapis.com/css2?family=Montserrat:wght@300;400&display=swap" rel="stylesheet">
<style>
  :root {
    --brand-blue: #1651a9;
    --brand-pink: #e0195b;
    --paper-white: #f2f2f2;
    --ink-white: #ffffff;
    --backdrop: #e4e5e7;
  }
  html, body {
    margin: 0;
    width: 1200px;
    height: 900px;
    overflow: hidden;
    background: var(--backdrop);
    font-family: "Montserrat", sans-serif;
  }
  .card {
    position: absolute;
    left: 290px;
    width: 620px;
    height: 354px;
    box-shadow: 0 6px 18px rgba(0,0,0,0.18);
    overflow: hidden;
  }
  .card-back {
    top: 70px;
    background: var(--brand-blue);
  }
  .card-back .brand-name {
    position: absolute;
    left: 0;
    right: 0;
    top: 50%;
    transform: translateY(-50%);
    text-align: center;
    color: var(--ink-white);
    font-weight: 300;
    font-size: 86px;
    letter-spacing: 6px;
  }
  .card-front {
    top: 476px;
    background: var(--brand-blue);
  }
  .brand-panel {
    position: absolute;
    left: 0;
    top: 0;
    width: 232px;
    height: 100%;
    background: var(--paper-white);
  }
  .brand-panel .brand-name {
    position: absolute;
    left: 116px;
    top: 177px;
    transform: translate(-50%, -50%) rotate(-90deg);
    white-space: nowrap;
    color: var(--brand-blue);
    font-weight: 300;
    font-size: 50px;
    letter-spacing: 3px;
  }
  .contact-panel {
    position: absolute;
    left: 268px;
    top: 62px;
    width: 320px;
    color: var(--ink-white);
  }
  .person-name {
    margin: 0;
    font-weight: 400;
    font-size: 22px;
    letter-spacing: 1.5px;
  }
  .person-role {
    margin: 2px 0 0;
    font-weight: 300;
    font-size: 15px;
  }
  .divider {
    margin: 16px 0 0;
    border: 0;
    border-top: 1px solid var(--ink-white);
    width: 100%;
  }
  .contact-list {
    margin: 44px 0 0;
    padding: 0;
    list-style: none;
    font-weight: 300;
    font-size: 16px;
    line-height: 22px;
  }
  .contact-list .label {
    display: inline-block;
    width: 22px;
  }
  .website {
    margin: 24px 0 0;
    color: var(--brand-pink);
    font-weight: 300;
    font-size: 16px;
  }
</style>
</head>
<body>
  <section class="card card-back">
    <div class="brand-name">JH PROMO</div>
  </section>

  <section class="card card-front">
    <div class="brand-panel">
      <div class="brand-name">JH PROMO</div>
    </div>
    <div class="contact-panel">
      <h1 class="person-name">LENA MARSH</h1>
      <p class="person-role">Operation Manager</p>
      <hr class="divider">
      <ul class="contact-list">
        <li><span class="label">T</span>0461528390</li>
        <li><span class="label">E</span>sales@jh-promo.com.au</li>
      </ul>
      <p class="website">www.jh-promo.com.au</p>
    </div>
  </section>
</body>
</html>
```